Loom Harbor needs a website

I sell rugs and carpet on my website, loomharborfloors.example. I need help with the site design to make it "pop". The logo in the header has been designed and I want the site to match it's style and color. Also I have some example sites for layout:
matvale.example
weave-quick.example

Industry/Entity Type

Carpet

Requirements
Must have
• Scrolling images on front page. I will insert photos, just need the code.

```html
<!DOCTYPE html>
<html lang="en">
<head>
<meta charset="utf-8">
<title>Loom Harbor — Rugs &amp; Flooring</title>
<link href="https://fonts.googleapis.com/css2?family=Open+Sans:wght@400;600;700&display=swap" rel="stylesheet">
<style>
:root{
  --navy:#1b3a68;
  --navy-dark:#163056;
  --green:#8fdc80;
  --green-bright:#6fd35a;
  --price:#2b5a22;
  --text:#333;
  --grey-band:#e6e6e6;
  --footer:#393939;
  --footer-deep:#2c2c2c;
  --bottom:#1f1f1f;
  --footer-text:#bdbdbd;
}
*{box-sizing:border-box;margin:0;padding:0}
html,body{width:907px;height:1200px;overflow:hidden}
body{position:relative;background:#fff;font-family:"Open Sans",sans-serif;color:var(--text)}
.abs{position:absolute}

/* header */
.brand{left:75px;top:38px;display:flex;align-items:center;gap:10px}
.brand-square{width:26px;height:26px;background:var(--navy)}
.brand-name{font-size:28px;font-weight:600;color:var(--navy);letter-spacing:.5px}
.search{left:514px;top:24px;width:141px;height:24px;border:1px solid #ccc;border-radius:2px;display:flex;align-items:center;padding-left:9px;font-size:10px;color:#999}
.search svg{position:absolute;right:5px;top:4px}
.checkout{left:666px;top:24px;width:78px;height:24px;background:var(--navy);color:#fff;border-radius:2px;font-size:12px;display:flex;align-items:center;justify-content:center}
.items{left:757px;top:28px;font-size:12px;color:#555}
.cart{left:804px;top:24px;width:27px;height:24px;background:var(--green-bright);border-radius:2px;display:flex;align-items:center;justify-content:center}
.nav{top:79px;left:386px;display:flex;gap:0;font-size:10.5px;text-transform:uppercase;color:#777}
.nav a{color:inherit;text-decoration:none;position:absolute;white-space:nowrap;top:0}
.nav a.active{color:var(--navy);font-weight:600}

/* hero */
.hero-band{left:0;top:112px;width:907px;height:237px;background:var(--grey-band)}
.hero-wood{left:75px;top:112px;width:237px;height:237px;background:linear-gradient(135deg,#6b3a1e,#b66a2c 45%,#c98d3c 70%,#b7a055)}
.hero-rugs{left:312px;top:112px;width:520px;height:237px;background:linear-gradient(120deg,#8a5a4a,#b22a2a 35%,#d8c7b8 65%,#8f3020)}
.hero-prev{left:75px;top:207px;width:37px;height:47px;background:rgba(30,30,30,.85);display:flex;align-items:center;justify-content:center}
.hero-caption{left:659px;top:166px;width:173px;height:121px;background:rgba(30,30,30,.85);padding:9px 0 0 13px;color:#fff}
.hero-caption .kicker{font-size:15px;font-weight:600;line-height:1}
.hero-caption .title{font-size:35px;font-weight:600;line-height:1.1;margin-top:4px}
.hero-caption .deal{font-size:35px;font-weight:600;line-height:1.05;color:var(--green-bright)}

/* sidebar */
.sidebar{left:75px;top:350px;width:182px;height:580px;background:var(--navy)}
.cat{position:absolute;left:7px;width:167px}
.cat-photo{height:102px}
.cat-label{height:30px;background:var(--green);display:flex;align-items:center;justify-content:center;font-size:13px;font-weight:600;color:#1d2d1a}

/* products */
.latest{left:272px;top:368px;font-size:19px;font-weight:600;color:#333}
.product{position:absolute;width:175px}
.product-photo{height:110px}
.product-name{margin-top:8px;font-size:12px;font-weight:600;color:var(--navy);line-height:1.2}
.product-price{font-size:10px;font-weight:600;color:var(--price);margin-top:3px}
.pager{left:274px;top:900px;display:flex;gap:1.6px}
.pager span{width:18px;height:17px;border-radius:3px;background:#d4d4d4;color:#888;font-size:8px;display:flex;align-items:center;justify-content:center}
.pager span.current{background:#777;color:#fff}

/* footer */
.footer{left:0;top:960px;width:907px;height:193px;background:linear-gradient(var(--footer),var(--footer-deep))}
.foot-head{font-size:12px;color:#eee;top:985px}
.foot-links{font-size:9.5px;color:var(--footer-text);line-height:19px;top:1009px;list-style:none}
.social{left:92px;top:1106px;display:flex;gap:4px}
.social span{width:22px;height:22px;background:#ccc;border-radius:2px;display:flex;align-items:center;justify-content:center}
.field{left:587px;width:175px;background:#262626;border:1px solid #444;border-radius:2px;font-size:9.5px;color:#777;padding:7px 9px}
.submit{left:768px;top:1105px;width:49px;height:23px;background:#5a5a5a;border-radius:2px;color:#ddd;font-size:9.5px;display:flex;align-items:center;justify-content:center}
.bottom{left:0;top:1153px;width:907px;height:47px;background:var(--bottom);color:#aaa;font-size:9.5px;display:flex;align-items:center;justify-content:center}
</style>
</head>
<body>

<header>
  <div class="abs brand"><span class="brand-square"></span><span class="brand-name">Loom Harbor</span></div>
  <div class="abs search">Search
    <svg width="15" height="15" viewBox="0 0 15 15"><circle cx="6" cy="6" r="4.5" fill="none" stroke="#888" stroke-width="1.6"/><line x1="9.4" y1="9.4" x2="13.5" y2="13.5" stroke="#888" stroke-width="1.8"/></svg>
  </div>
  <div class="abs checkout">Check out</div>
  <div class="abs items">0 items</div>
  <div class="abs cart"><svg width="15" height="12" viewBox="0 0 15 12"><path d="M1 4h13l-2 7H3z" fill="#fff"/><path d="M4 4l3-3M11 4L8 1" stroke="#fff" stroke-width="1.2"/></svg></div>
  <nav class="abs nav">
    <a class="active" style="left:0">Home</a>
    <a style="left:58px">About us</a>
    <a style="left:135px">Products</a>
    <a style="left:216px">Specials</a>
    <a style="left:288px">Contact us</a>
    <a style="left:378px">My account</a>
  </nav>
</header>

<section class="hero">
  <div class="abs hero-band"></div>
  <div class="abs hero-wood" role="img" aria-label="Hardwood floor plank samples"></div>
  <div class="abs hero-rugs" role="img" aria-label="Stack of patterned oriental rugs"></div>
  <div class="abs hero-prev"><svg width="16" height="28" viewBox="0 0 16 28"><path d="M14 1L2 14l12 13" fill="none" stroke="#fff" stroke-width="1.5"/></svg></div>
  <div class="abs hero-caption">
    <div class="kicker">NAM AC MASSA VEL</div>
    <div class="title">MAURIS</div>
    <div class="deal">15% OFF</div>
  </div>
</section>

<aside class="abs sidebar">
  <div class="cat" style="top:10px"><div class="cat-photo" role="img" aria-label="Commercial lounge with cushions on wood floor" style="background:linear-gradient(135deg,#a57a55,#3d3f48 60%,#c6b49a)"></div><div class="cat-label">Commercial Flooring</div></div>
  <div class="cat" style="top:153px"><div class="cat-photo" role="img" aria-label="Living room sofa on shaggy carpet" style="background:linear-gradient(#e6e2dc,#c9b899 60%,#a89478)"></div><div class="cat-label">Carpet Flooring</div></div>
  <div class="cat" style="top:296px"><div class="cat-photo" role="img" aria-label="Open dining room with hardwood floor" style="background:linear-gradient(135deg,#5a544c,#2d3e5c 45%,#c2b7a8)"></div><div class="cat-label">Harwood Flooring</div></div>
  <div class="cat" style="top:438px"><div class="cat-photo" role="img" aria-label="Red oriental area rugs" style="background:linear-gradient(135deg,#b8302a,#7d1e1e 50%,#c44a35)"></div><div class="cat-label">Area Rugs</div></div>
</aside>

<main>
  <h2 class="abs latest">LATEST PRODUCTS</h2>

  <div class="product" style="left:273px;top:402px"><div class="product-photo" role="img" aria-label="Light hickory plank sample" style="background:linear-gradient(135deg,#d8b070,#efd09a 50%,#c99955)"></div><div class="product-name">AMERICAN HICKORY</div><div class="product-price">Price: $9.39 per SF</div></div>
  <div class="product" style="left:465px;top:402px"><div class="product-photo" role="img" aria-label="Dark hickory plank sample" style="background:linear-gradient(135deg,#5c4320,#a07d45 50%,#6b5130)"></div><div class="product-name">AMERICAN HICKORY</div><div class="product-price">Price: $9.39 per SF</div></div>
  <div class="product" style="left:657px;top:402px"><div class="product-photo" role="img" aria-label="Bordered oriental rug" style="background:radial-gradient(#a0a58a,#8a8a6e 55%,#7a4a2c)"></div><div class="product-name">AMERICAN HICKORY</div><div class="product-price">Price: $9.39 per SF</div></div>

  <div class="product" style="left:273px;top:568px"><div class="product-photo" role="img" aria-label="Floral patterned carpet" style="background:linear-gradient(135deg,#5a4535,#9aa6a0 50%,#5a4535)"></div><div class="product-name">AMERICAN HICKORY</div><div class="product-price">Price: $9.39 per SF</div></div>
  <div class="product" style="left:465px;top:568px"><div class="product-photo" role="img" aria-label="Reddish hardwood plank sample" style="background:linear-gradient(135deg,#9c4a1c,#c7733a 50%,#a4521f)"></div><div class="product-name">AMERICAN HICKORY</div><div class="product-price">Price: $9.39 per SF</div></div>
  <div class="product" style="left:657px;top:568px"><div class="product-photo" role="img" aria-label="Olive leaf patterned carpet" style="background:linear-gradient(135deg,#7c7a55,#b5b088 50%,#6f6c4a)"></div><div class="product-name">AMERICAN HICKORY</div><div class="product-price">Price: $9.39 per SF</div></div>

  <div class="product" style="left:273px;top:734px"><div class="product-photo" role="img" aria-label="Damask patterned carpet" style="background:linear-gradient(135deg,#4a4236,#a8997a 50%,#4a4236)"></div><div class="product-name">AMERICAN HICKORY</div><div class="product-price">Price: $9.39 per SF</div></div>
  <div class="product" style="left:465px;top:734px"><div class="product-photo" role="img" aria-label="Paisley patterned carpet" style="background:linear-gradient(135deg,#8a8470,#a06a5a 50%,#9a9a80)"></div><div class="product-name">AMERICAN HICKORY</div><div class="product-price">Price: $9.39 per SF</div></div>
  <div class="product" style="left:657px;top:734px"><div class="product-photo" role="img" aria-label="Tan paisley carpet" style="background:linear-gradient(135deg,#6e6448,#9a8e6a 50%,#74694b)"></div><div class="product-name">AMERICAN HICKORY</div><div class="product-price">Price: $9.39 per SF</div></div>

  <div class="abs pager"><span class="current">1</span><span>2</span><span>3</span><span>4</span><span>5</span><span>6</span><span>7</span><span>8</span></div>
</main>

<footer>
  <div class="abs footer"></div>
  <h3 class="abs foot-head" style="left:91px;font-weight:400">Navigation Menu</h3>
  <ul class="abs foot-links" style="left:91px"><li>Home</li><li>About us</li><li>Products</li><li>Specials</li></ul>
  <ul class="abs foot-links" style="left:171px"><li>Contact us</li><li>My Accountus</li><li>Register</li><li>Login</li></ul>
  <h3 class="abs foot-head" style="left:289px;font-weight:400">Support Links</h3>
  <ul class="abs foot-links" style="left:289px"><li>Privacy Policy</li><li>Terms and Conditions</li><li>Customer Support</li><li>FAQ</li></ul>
  <h3 class="abs foot-head" style="left:463px;font-weight:400">About us</h3>
  <ul class="abs foot-links" style="left:463px"><li>My Account</li><li>Shipping Policy</li><li>Sitemap</li><li>Cart Help</li></ul>
  <h3 class="abs foot-head" style="left:589px;font-weight:400">Contact us</h3>
  <div class="abs field" style="top:1016px;height:28px">Name</div>
  <div class="abs field" style="top:1048px;height:28px">E-mail</div>
  <div class="abs field" style="top:1080px;height:51px">Comment</div>
  <div class="abs submit">SUBMIT</div>
  <div class="abs social">
    <span></span><span></span><span></span>
    <span><svg width="12" height="9" viewBox="0 0 12 9"><rect x=".5" y=".5" width="11" height="8" fill="none" stroke="#555"/><path d="M.5.5L6 5l5.5-4.5" fill="none" stroke="#555"/></svg></span>
    <span></span>
  </div>
  <div class="abs bottom">Copyright © 2014 Loom Harbor, LLC. &nbsp;All rights reserved.</div>
</footer>

</body>
</html>
```